Australian Civil Construction, Quarry & Mining Services needs a business card

We need a business card designed for our Civil Construction, Quarry & Mining Services based in the country in Australia.
Our Company Brackley Earthworks provide innovate solutions for infrastructure, agricultural and mining (aggregate, sand, roadbase) industry.
We would like our business cards to be double sided
Front of card: black background or something that resembles our business colours. (it doesn't have to be black we are open to options)
- Company name - Brackley Earthworks
- Either our logo or some sort of icon/picture that resembles our business
- Website - https://brackleyearthworks.com.au/
- We will have a number of different names, positions descriptions, phone numbers and emails on separate cards for each of our managers/directors

```html
<!DOCTYPE html>
<html lang="en">
<head>
<meta charset="utf-8">
<title>Brackley Earthworks – Business Card</title>
<link href="https://fonts.googleapis.com/css2?family=Roboto:wght@400;500;700&display=swap" rel="stylesheet">
<style>
  :root {
    --stage: #1c1c1e;
    --card-black: #141213;
    --orange: #d95d1c;
    --orange-bright: #f07c1e;
    --white: #ffffff;
    --pattern-dark: #1d1b1c;
    --pattern-light: #2a2728;
  }
  * { margin: 0; padding: 0; box-sizing: border-box; }
  html, body {
    width: 1200px; height: 900px; overflow: hidden;
    background: var(--stage);
    font-family: "Roboto", Arial, sans-serif;
  }
  .stage {
    width: 1200px; height: 900px;
    display: flex; flex-direction: column;
    align-items: center; justify-content: center; gap: 40px;
  }
  .card {
    position: relative; width: 660px; height: 377px;
    overflow: hidden; border-radius: 4px;
    box-shadow: 0 12px 30px rgba(0,0,0,.55);
  }

  /* Front */
  .card-front { background: var(--orange); }
  .front-curve { position: absolute; inset: 0; width: 100%; height: 100%; }
  .contact-block {
    position: absolute; left: 40px; top: 46px; color: var(--white);
  }
  .person-name {
    font-size: 30px; font-weight: 500; letter-spacing: .5px; line-height: 1;
    text-transform: uppercase;
  }
  .person-role {
    font-size: 13px; font-weight: 400; letter-spacing: .6px;
    text-transform: uppercase; margin-top: 4px;
  }
  .address { margin-top: 16px; font-size: 13px; line-height: 1.45; }
  .contact-list { list-style: none; margin-top: 12px; font-size: 13px; line-height: 1.6; }
  .contact-list li { display: flex; align-items: center; gap: 7px; }
  .contact-list svg { width: 12px; height: 12px; flex: none; }

  .front-brand {
    position: absolute; right: 48px; bottom: 92px;
    display: flex; align-items: center; gap: 12px;
  }
  .brand-dot {
    width: 34px; height: 34px; border-radius: 50%; background: var(--orange-bright);
  }
  .brand-name {
    color: var(--white); font-weight: 700; font-size: 22px;
    letter-spacing: 3px; text-transform: uppercase; line-height: 1.15;
  }

  /* Back */
  .card-back { background: var(--card-black); }
  .back-pattern {
    position: absolute; inset: 0;
    background: linear-gradient(135deg, var(--pattern-light) 0%, var(--pattern-dark) 55%, var(--card-black) 100%);
  }
  .back-brand {
    position: absolute; right: 44px; bottom: 50px;
    color: var(--white); font-weight: 700; font-size: 30px;
    letter-spacing: 4px; text-transform: uppercase; line-height: 1.15;
    text-align: right;
  }
</style>
</head>
<body>
<main class="stage">

  <section class="card card-front" aria-label="Business card front">
    <svg class="front-curve" viewBox="0 0 660 377" preserveAspectRatio="none" aria-hidden="true">
      <path d="M430 0 C320 50 270 230 372 377 L660 377 L660 0 Z" fill="#ffffff"/>
      <path d="M442 0 C334 54 286 232 386 377 L660 377 L660 0 Z" fill="#141213"/>
    </svg>

    <div class="contact-block">
      <h1 class="person-name">Daniel Whitford</h1>
      <p class="person-role">President</p>
      <p class="address">14 Kelso Lane, Tarrawong<br>Victoria 3712, Australia</p>
      <ul class="contact-list">
        <li>
          <svg viewBox="0 0 24 24" aria-hidden="true"><path fill="#fff" d="M6.6 10.8a15 15 0 0 0 6.6 6.6l2.2-2.2a1 1 0 0 1 1-.25 11.4 11.4 0 0 0 3.6.57 1 1 0 0 1 1 1V20a1 1 0 0 1-1 1A17 17 0 0 1 3 4a1 1 0 0 1 1-1h3.5a1 1 0 0 1 1 1c0 1.25.2 2.45.57 3.57a1 1 0 0 1-.25 1z"/></svg>
          03 5901 2288
        </li>
        <li>
          <svg viewBox="0 0 24 24" aria-hidden="true"><rect x="2" y="5" width="20" height="14" rx="1" fill="none" stroke="#fff" stroke-width="2"/><path d="M2 6l10 7 10-7" fill="none" stroke="#fff" stroke-width="2"/></svg>
          admin@brackleyearthworks.com.au
        </li>
        <li>
          <svg viewBox="0 0 24 24" aria-hidden="true"><circle cx="12" cy="12" r="9.5" fill="none" stroke="#fff" stroke-width="2"/><path d="M2.5 12h19M12 2.5c3 3 3 16 0 19M12 2.5c-3 3-3 16 0 19" fill="none" stroke="#fff" stroke-width="1.6"/></svg>
          brackleyearthworks.com.au
        </li>
      </ul>
    </div>

    <div class="front-brand">
      <span class="brand-dot" aria-hidden="true"></span>
      <p class="brand-name">Brackley<br>Earthworks</p>
    </div>
  </section>

  <section class="card card-back" aria-label="Business card back">
    <div class="back-pattern" role="img" aria-label="Repeating pattern of the company symbol in dark tones"></div>
    <p class="back-brand">Brackley<br>Earthworks</p>
  </section>

</main>
</body>
</html>
```